Improved Business Card, Government Contracting

We are looking to update the design of our business cards. We would like to create a template that can be used for future employees and easy to update.

Halvorsen Advisory Partners, LLC is a Service Disabled Veteran Owned Small Business with headquarters located in Leavenworth, KS. Our current website is www.hapteam.com. We have contracts in KS and VA with expansion opportunities in various other states. Our primary line of work is within government contracting and providing consulting services to various organizations within the Bureau of Frontier Works. We would like to project a professional image of our company that is consistent with the industry. Provided are previous versions of our business card template that shows our logo as well. We would like to make sure the information on the cards are easily noticeable .

Target Market(s)

Government Officials
Fellow Small Business Contractors
Large Business Contractors (ex. TRUX, Keswell Barnaby, Pryde Okonjo Whitcombe)

Industry/Entity Type

Business

Contact Information for Business Card

Dale Fenwick
Office Manager
Halvorsen Advisory Partners
Ph: 913.555.0172
Email: d.fenwick@hapteam.us
www.hapteam.com

Requirements
Must have
• The business mailing address is:
• 31842 204th Lane
• Leavenworth, KS 66099
Nice to have
• Embossed lettering

```html
<!DOCTYPE html>
<html lang="en">
<head>
<meta charset="utf-8">
<title>Halvorsen Advisory Partners – Business Card</title>
<link href="https://fonts.googleapis.com/css2?family=Open+Sans:wght@400;600;700&display=swap" rel="stylesheet">
<style>
  :root {
    --navy: #28298a;
    --yellow: #ece51e;
    --paper: #ffffff;
    --ink: #2b2b2b;
    --backdrop: #a3a39e;
    --band: #ffffff;
  }
  * { margin: 0; padding: 0; box-sizing: border-box; }
  html, body { width: 1200px; height: 1000px; overflow: hidden; }
  body {
    font-family: "Open Sans", Arial, sans-serif;
    background: var(--band);
    position: relative;
  }
  .stage {
    position: absolute; left: 0; top: 0;
    width: 1200px; height: 860px;
    background: var(--backdrop);
  }
  .card {
    position: absolute;
    left: 320px;
    width: 560px; height: 320px;
    box-shadow: 0 6px 18px rgba(0,0,0,.18);
    overflow: hidden;
  }
  /* Card front: company side */
  .card-front { top: 80px; background: var(--navy); }
  .front-name {
    position: absolute; left: 0; right: 0; top: 98px;
    text-align: center; color: var(--yellow);
    font-weight: 400; text-transform: uppercase;
  }
  .front-name .line-1 { display: block; font-size: 38px; letter-spacing: 2px; line-height: 1.1; }
  .front-name .line-2 { display: block; font-size: 20px; letter-spacing: 4px; line-height: 1.4; }
  .front-web {
    position: absolute; right: 40px; bottom: 36px;
    color: var(--yellow); font-size: 15px; font-weight: 400;
  }
  /* Card back: contact side */
  .card-back { top: 460px; background: var(--paper); }
  .block { position: absolute; background: var(--navy); }
  .block-top { left: 0; top: 30px; width: 130px; height: 110px; }
  .block-bottom { left: 150px; top: 200px; width: 170px; height: 120px; }
  .back-mark {
    position: absolute; left: 118px; top: 148px;
    color: var(--navy); font-size: 30px; font-weight: 700; letter-spacing: 1px;
  }
  .contact { position: absolute; left: 350px; top: 40px; color: var(--ink); }
  .contact .person { color: var(--navy); font-size: 18px; font-weight: 700; line-height: 1.2; }
  .contact .role { font-size: 14px; margin-bottom: 30px; }
  .contact .line { font-size: 13px; line-height: 1.5; white-space: nowrap; }
  .contact .line b { font-weight: 700; display: inline-block; width: 15px; }
  .band-mark {
    position: absolute; right: 56px; top: 896px;
    color: var(--navy); font-size: 34px; font-weight: 700; letter-spacing: 1px;
  }
</style>
</head>
<body>
  <main class="stage">
    <section class="card card-front" aria-label="Card front">
      <h1 class="front-name">
        <span class="line-1">Halvorsen</span>
        <span class="line-2">Advisory Partners</span>
      </h1>
      <p class="front-web">www.hapteam.com</p>
    </section>

    <section class="card card-back" aria-label="Card back">
      <div class="block block-top"></div>
      <div class="block block-bottom"></div>
      <p class="back-mark">HAP</p>
      <div class="contact">
        <p class="person">Dale Fenwick</p>
        <p class="role">Office Manager</p>
        <p class="line"><b>T</b>913.555.0172</p>
        <p class="line"><b>F</b>913.555.0163</p>
        <p class="line"><b>E</b>d.fenwick@hapteam.us</p>
        <p class="line">31842 204th Lane</p>
        <p class="line">Leavenworth, KS 66099</p>
      </div>
    </section>
  </main>
  <p class="band-mark">HAP</p>
</body>
</html>
```